Web Design for an Employment Agency

We need a website design for an employment agency here in New Zealand.

We have attached a few examples of what other designers have submitted but the client is not exactly happy with the concepts and what came out in the end.

They have given this link for some idea of the sketches look they like: http://www.brindlequay.com/painter-merges-beasts-with-forest-ink-drawings/

They have asked to use "maori sketches" in black and white through the website, you can Google "Maori art" or "Maori drawings" to get an idea of the type of drawings that they are.

Please ensure the concept designs incorporate some sort of those maori designs through out the website.

Unfortunately we do not have a lot of copy to work with, but please use filler text and content for areas if need be and we can get extra copy from the client afterwards.

The client does not want people or buildings

Also, the logo should be displayed as it is currently – they do not want to deviate from it.

They also would like Maori type of sketches (in Black and white) the grey colour can be used as a background when you use the logo on the page.

The design must be professional and bold.

The service they offer is all about professionalism.

------------------------------------------------------------------
UPDATE - 20th FEBRUARY

Please see attached file for the brief of the different sections of the website as well as some examples of the maori designs from plumvaultpix.

I have also attached another design she liked the look of the most, but se wanted the following changes made to it:

- She does not want the photo at the top with the hand writing, she wants her logo in a watermark format to show there in the background
- She wants where you have those other images in circle, she wants "maori" type designs to be incorporated somewhere there
- She needs the content that we have provided to be all there on the page in the different sections, I will re-send you the content

Please re-submit your concepts based along the lines of that, please ensure the text and content match the sections and I will send to her for final approval.

Updates

Looking for designs to come through ASAP please

Target Market(s)

New Zealand people looking for jobs, and people looking for workers in NZ

Industry/Entity Type

Employment Agency

Number of Pages Required

4 page

Font styles to use
Sans Serif

Colors

Designer to choose colors to be used in the design.

Requirements
Must have
• It needs to be nice and clean perhaps grey scale like the attached
• The design must be professional and bold.
• They also would like Maori type of sketches (in Black and white) the grey colour can be used as a background when you use the logo on the page.
Nice to have
• You can think about the business, maybe do some of the copy or content as well to make more attractive to the client when I show them
Should not have
• Do not have lots of colour, The client does not want people or buildings

```html
<!DOCTYPE html>
<html lang="en">
<head>
<meta charset="utf-8">
<title>Hireward.net – Employment Agency</title>
<link href="https://fonts.googleapis.com/css2?family=Open+Sans:wght@400;600;700;800&display=swap" rel="stylesheet">
<style>
:root{
  --ink:#1d1d1d;
  --text:#3a3a3a;
  --muted:#6d6d6d;
  --soft:#f3f1f1;
  --panel:#ebe8e8;
  --line:#cfcaca;
  --white:#ffffff;
  --dark:#1e1e1e;
}
*{box-sizing:border-box;margin:0;padding:0}
html,body{width:1200px;height:5014px;overflow:hidden}
body{position:relative;background:var(--white);font-family:"Open Sans",Arial,sans-serif;color:var(--text)}
.abs{position:absolute}
.band{position:absolute;left:0;width:1200px}
.band-soft{background:var(--soft)}
.band-dark{background:var(--dark)}
.center{text-align:center}
.watermark{left:380px;top:30px;width:440px;height:440px;border-radius:50%;background:radial-gradient(circle,#ebe8e8 0%,rgba(235,232,232,0) 70%)}
.brand-badge{width:160px;height:160px;border-radius:50%;background:var(--panel);border:6px solid var(--white);box-shadow:0 0 0 1px var(--line);display:flex;align-items:center;justify-content:center;font-weight:700;font-size:22px;color:var(--ink)}
.hero-title{left:0;width:1200px;top:226px;font-size:26px;font-weight:800;color:var(--ink);letter-spacing:1px}
.hero-sub{left:0;width:1200px;top:266px;font-size:17px;color:var(--text)}
.hero-cta{left:0;width:1200px;top:312px;font-size:15px;font-weight:800;color:var(--ink);letter-spacing:1px}
.ornament{width:70px;height:14px;border-radius:7px;background:linear-gradient(90deg,#bbb,#555,#bbb)}
.feature{width:240px;font-size:15px;line-height:1.35;color:var(--text)}
.feature svg{display:block;margin-bottom:16px}
.section-head{left:425px;width:350px;height:66px;border:2px solid var(--ink);border-radius:33px;display:flex;align-items:center;justify-content:center;font-size:24px;font-weight:800;color:var(--ink);letter-spacing:1px;background:transparent}
.section-head::before,.section-head::after{content:"";position:absolute;top:50%;width:60px;height:2px;background:var(--ink)}
.section-head::before{left:-70px}.section-head::after{right:-70px}
.art-circle{border-radius:50%}
.art-bulbs{background:radial-gradient(circle at 50% 45%,#3a3a3a 0%,#1b1b1b 62%,#bdb9b9 64%,#e6e3e3 100%)}
.art-keys{background:radial-gradient(circle at 45% 50%,#f4f4f4 0%,#cfcfcf 60%,#a9a6a6 64%,#e6e3e3 100%)}
.art-circuit{background:radial-gradient(circle at 50% 50%,#4a4a4a 0%,#101010 62%,#bdb9b9 64%,#e6e3e3 100%)}
.corner-art{width:120px;height:90px;background:linear-gradient(135deg,#d0cccc,rgba(208,204,204,0))}
.sub-head{font-size:17px;font-weight:800;color:var(--ink);letter-spacing:.5px;line-height:1.35}
.body-text{font-size:15px;line-height:1.6;color:var(--text)}
.story-text{font-size:14px;line-height:1.55;color:var(--text)}
.quote-big{font-size:28px;font-weight:800;color:var(--ink)}
.list-item{display:flex;align-items:center;gap:18px;font-size:15px;line-height:1.4;color:var(--text)}
.num{flex:none;width:36px;height:36px;border-radius:50%;background:#d6d2d2;color:var(--white);font-size:13px;font-weight:700;display:flex;align-items:center;justify-content:center}
.service-card{background:var(--white);height:190px;padding:34px 30px;display:flex;gap:26px;box-shadow:0 1px 4px rgba(0,0,0,.06)}
.service-card h4{font-size:16px;font-weight:800;color:var(--ink);margin-bottom:10px}
.service-card p{font-size:13px;line-height:1.5;color:var(--text)}
.icon-ring{flex:none;width:80px;height:80px;border-radius:50%;border:2px solid var(--ink);display:flex;align-items:center;justify-content:center}
.service-icon{width:180px;text-align:center;font-size:15px;line-height:1.4;color:var(--text)}
.service-icon .ring{width:100px;height:100px;border-radius:50%;border:2px solid var(--ink);margin:0 auto 24px;display:flex;align-items:center;justify-content:center}
.rule{height:1px;background:var(--line)}
.testimonial{background:var(--white);border:1px solid var(--line);height:275px;padding:40px 42px}
.testimonial .mark{font-size:56px;line-height:.8;color:#b9b5b5;font-weight:800}
.testimonial p{font-size:14px;line-height:1.55;color:var(--text);margin-top:8px}
.testimonial .dash{width:30px;height:2px;background:var(--line);margin:20px 0 10px}
.testimonial .who{font-size:14px;font-weight:800;color:var(--ink)}
.arrow{font-size:30px;color:#9a9696}
.map{left:143px;top:4155px;width:569px;height:365px;background:linear-gradient(135deg,#e7e5e2,#d8dcd5 55%,#e4e2df)}
.form{left:752px;top:4155px;width:304px;height:491px;background:var(--soft);padding:26px 26px}
.form h5{font-size:13px;font-weight:800;color:var(--ink)}
.field{height:34px;background:var(--white);border:1px solid var(--line);margin-top:12px;font-size:11px;color:var(--muted);padding:10px 12px}
.field-tall{height:128px}
.submit{margin-top:14px;height:40px;background:var(--ink);color:var(--white);font-weight:800;font-size:14px;display:flex;align-items:center;justify-content:center;letter-spacing:1px}
.contact-item{display:flex;align-items:center;gap:16px;font-size:13px;line-height:1.35;color:var(--ink);font-weight:700}
.contact-item .ico{width:40px;height:40px;border-radius:50%;border:1.5px solid var(--ink);display:flex;align-items:center;justify-content:center;flex:none}
.follow{left:0;width:1200px;top:4874px;display:flex;justify-content:center;align-items:center;gap:14px;color:var(--white);font-size:12px;font-weight:800;letter-spacing:1px}
.social{width:30px;height:30px;border-radius:50%;background:#8c8c8c}
.copyright{left:0;width:1200px;top:4940px;font-size:11px;color:#9c9c9c}
</style>
</head>
<body>

<!-- Hero -->
<section class="band band-soft" style="top:0;height:692px">
  <div class="abs watermark" role="img" aria-label="Faint watermark of the agency brand in the background"></div>
  <div class="abs brand-badge" style="left:520px;top:40px">Hireward.net</div>
  <h1 class="abs hero-title center">WHY – HIREWARD.NET ?</h1>
  <p class="abs hero-sub center">Applying for positions and not getting anywhere.......</p>
  <p class="abs hero-cta center">LET US HELP YOU!</p>
  <div class="abs ornament" role="img" aria-label="Small Maori-style ornament" style="left:565px;top:345px"></div>

  <div class="abs feature" style="left:82px;top:515px">
    <svg width="46" height="46" viewBox="0 0 46 46"><circle cx="15" cy="15" r="5" fill="#1d1d1d"/><circle cx="31" cy="15" r="5" fill="#1d1d1d"/><circle cx="23" cy="26" r="5" fill="#1d1d1d"/><path d="M7 34q8-10 16 0M23 34q8-10 16 0M14 44q9-12 18 0" fill="#1d1d1d"/></svg>
    Face to face meeting –<br>YOU ARE NOT ALONE ANYMORE
  </div>
  <div class="abs feature" style="left:425px;top:515px">
    <svg width="46" height="46" viewBox="0 0 46 46"><circle cx="23" cy="12" r="8" fill="#1d1d1d"/><path d="M9 44q0-22 14-22t14 22z" fill="#1d1d1d"/></svg>
    Represent yourself<br>professionally
  </div>
  <div class="abs feature" style="left:690px;top:515px">
    <svg width="46" height="46" viewBox="0 0 46 46"><rect x="2" y="2" width="42" height="42" rx="8" fill="#1d1d1d"/><circle cx="20" cy="20" r="9" fill="none" stroke="#fff" stroke-width="3"/><path d="M27 27l9 9" stroke="#fff" stroke-width="4"/></svg>
    Where to begin<br>searching
  </div>
  <div class="abs feature" style="left:895px;top:515px">
    <svg width="46" height="46" viewBox="0 0 46 46"><circle cx="23" cy="12" r="8" fill="#1d1d1d"/><path d="M9 44q0-22 14-22t14 22z" fill="#1d1d1d"/><path d="M21 24l2 4 2-4-2 14z" fill="#fff"/></svg>
    Having an agent that<br>acts on your behalf
  </div>
</section>

<!-- About -->
<section class="band" style="top:692px;height:722px">
  <div class="abs corner-art" role="img" aria-label="Maori-style corner pattern" style="left:0;top:0"></div>
  <div class="abs section-head" style="top:68px">ABOUT US</div>
  <div class="abs art-circle art-bulbs" role="img" aria-label="Black and white sketch of hanging light bulbs in a circle framed by Maori patterns" style="left:135px;top:200px;width:400px;height:400px"></div>
  <h3 class="abs sub-head" style="left:592px;top:205px">OUR STORY</h3>
  <div class="abs ornament" role="img" aria-label="Small Maori-style ornament" style="left:592px;top:236px;width:50px"></div>
  <div class="abs" style="left:592px;top:275px;width:430px">
    <p class="story-text">20 years in the Recruitment market – as Candidate, Employer, External &amp; Internal Recruiter - highlighted certain annoying facts about the Recruitment Industry that screamed for a solution!</p>
    <p class="story-text" style="margin-top:14px">After more than 5 years of market research a service addressing the needs of Job Seekers (Candidates) could not be found and we have decided that the question so many candidates ask .....</p>
    <p class="quote-big" style="margin-top:22px">“Can you find me a job.....?”</p>
    <p class="story-text" style="margin-left:14px">definitely needed a POSITIVE answer.</p>
    <p class="story-text" style="margin-top:20px">By offering the service namely, becoming the Job Seekers agent in the employment market, we not only assist our clients (the candidates) BUT we inevitably address the frustrations of the Employers and Recruiters successfully as well.</p>
  </div>
</section>

<!-- Goals & frustrations -->
<section class="band band-soft" style="top:1414px;height:1411px">
  <div class="abs corner-art" role="img" aria-label="Maori-style corner pattern" style="left:0;top:0"></div>
  <h3 class="abs sub-head" style="left:147px;top:60px;width:430px;font-size:19px">THE CANDIDATE’S MAIN GOALS FOR HIS/ HER JOB SEARCH IS USUALLY ONE OF THREE FACTORS</h3>
  <div class="abs ornament" role="img" aria-label="Small Maori-style ornament" style="left:147px;top:160px;width:50px"></div>
  <div class="abs list-item" style="left:147px;top:196px;width:360px"><span class="num">01</span>To find a suitable position – which is usually paramount</div>
  <div class="abs list-item" style="left:147px;top:270px;width:360px"><span class="num">02</span>To find a position that is a step up the career ladder from the current</div>
  <div class="abs list-item" style="left:147px;top:344px;width:360px"><span class="num">03</span>To find a position offering a better remuneration package</div>
  <div class="abs art-circle art-keys" role="img" aria-label="Black and white image of a magnifying glass over keyboard keys in a circle framed by Maori patterns" style="left:640px;top:56px;width:390px;height:390px"></div>

  <div class="abs art-circle art-circuit" role="img" aria-label="Dark circuit board pattern in a circle framed by Maori patterns" style="left:147px;top:558px;width:388px;height:388px"></div>
  <h3 class="abs sub-head" style="left:652px;top:575px;width:380px;font-size:19px">THE EMPLOYER / RECRUITER’S MAIN FRUSTRATIONS:</h3>
  <div class="abs ornament" role="img" aria-label="Small Maori-style ornament" style="left:652px;top:640px;width:50px"></div>
  <div class="abs list-item" style="left:652px;top:698px;width:360px"><span class="num">01</span>Incomplete CV’s</div>
  <div class="abs list-item" style="left:652px;top:771px;width:360px"><span class="num">02</span>Unreliable information</div>
  <div class="abs list-item" style="left:652px;top:845px;width:340px"><span class="num">03</span>Candidates not understanding the job specification</div>

  <h3 class="abs sub-head center" style="left:0;width:1200px;top:1022px;font-size:20px">OUR SERVICE PROVIDES</h3>
  <div class="abs ornament" role="img" aria-label="Small Maori-style ornament" style="left:575px;top:1062px;width:50px"></div>
  <div class="abs service-card" style="left:147px;top:1137px;width:441px">
    <div class="icon-ring"><svg width="34" height="34" viewBox="0 0 34 34"><rect x="7" y="3" width="20" height="26" fill="none" stroke="#1d1d1d" stroke-width="2"/><circle cx="17" cy="12" r="4" fill="#1d1d1d"/><path d="M11 23q6-8 12 0" fill="#1d1d1d"/></svg></div>
    <div><h4>TO CANDIDATES</h4><p>Clear direction and understanding of the job market and opens up opportunities that they most possibly were either not aware of or did not know how to pursue.</p></div>
  </div>
  <div class="abs service-card" style="left:612px;top:1137px;width:444px">
    <div class="icon-ring"><svg width="40" height="34" viewBox="0 0 40 34"><path d="M2 16q18-16 36 0z" fill="#1d1d1d"/><path d="M20 16v14" stroke="#1d1d1d" stroke-width="2"/><circle cx="12" cy="24" r="3" fill="#1d1d1d"/><circle cx="20" cy="24" r="3" fill="#1d1d1d"/><circle cx="28" cy="24" r="3" fill="#1d1d1d"/></svg></div>
    <div><h4>TO EMPLOYERS</h4><p>we offer screened and well represented candidates at no fee</p></div>
  </div>
  <div class="abs corner-art" role="img" aria-label="Maori-style corner pattern" style="left:1080px;top:1321px;transform:rotate(180deg)"></div>
</section>

<!-- Services -->
<section class="band" style="top:2825px;height:611px">
  <div class="abs section-head" style="top:68px">SERVICES</div>
  <p class="abs center body-text" style="left:0;width:1200px;top:180px">We provide tailormade packages or our standard complete service</p>
  <div class="abs rule" style="left:380px;top:170px;width:440px"></div>
  <div class="abs service-icon" style="left:110px;top:258px"><div class="ring"><svg width="40" height="36" viewBox="0 0 40 36"><path d="M4 4h32v22H16l-8 8v-8H4z" fill="#1d1d1d"/><circle cx="13" cy="15" r="2.5" fill="#fff"/><circle cx="20" cy="15" r="2.5" fill="#fff"/><circle cx="27" cy="15" r="2.5" fill="#fff"/></svg></div>Interview /<br>Consultation</div>
  <div class="abs service-icon" style="left:305px;top:258px"><div class="ring"><svg width="40" height="36" viewBox="0 0 40 36"><rect x="4" y="4" width="32" height="28" fill="none" stroke="#1d1d1d" stroke-width="2"/><circle cx="14" cy="15" r="4" fill="#1d1d1d"/><path d="M8 26q6-8 12 0z" fill="#1d1d1d"/><path d="M23 12h9M23 18h9M23 24h9" stroke="#1d1d1d" stroke-width="2"/></svg></div>Professional<br>CV Writing</div>
  <div class="abs service-icon" style="left:505px;top:258px"><div class="ring"><svg width="42" height="36" viewBox="0 0 42 36"><path d="M4 13h8l16-9v28l-16-9H4z" fill="#1d1d1d"/><path d="M10 23l4 10h5l-3-10z" fill="#1d1d1d"/><path d="M32 12q4 6 0 12M36 8q7 10 0 20" stroke="#1d1d1d" stroke-width="2" fill="none"/></svg></div>Marketing<br>the candidate</div>
  <div class="abs service-icon" style="left:712px;top:258px"><div class="ring"><svg width="36" height="40" viewBox="0 0 36 40"><rect x="5" y="5" width="26" height="32" fill="none" stroke="#1d1d1d" stroke-width="2"/><rect x="12" y="2" width="12" height="6" fill="#1d1d1d"/><path d="M10 16h4M10 23h4M10 30h4M17 16h10M17 23h10M17 30h10" stroke="#1d1d1d" stroke-width="2"/></svg></div>Self-listing<br>suggestions</div>
  <div class="abs service-icon" style="left:913px;top:258px"><div class="ring"><svg width="40" height="40" viewBox="0 0 40 40"><circle cx="20" cy="20" r="16" fill="none" stroke="#1d1d1d" stroke-width="2.5"/><path d="M12 20l6 6 11-12" fill="none" stroke="#1d1d1d" stroke-width="3"/></svg></div>2 Written<br>references done</div>
  <div class="abs rule" style="left:285px;top:495px;width:630px"></div>
  <p class="abs center body-text" style="left:0;width:1200px;top:505px;font-size:14px">The first Consultation is free so give us a call or drop us a mail to find the best solution for you</p>
</section>

<!-- Testimonials -->
<section class="band band-soft" style="top:3436px;height:575px">
  <div class="abs section-head" style="top:64px">TESTIMONIALS</div>
  <div class="abs arrow" style="left:80px;top:288px">‹</div>
  <div class="abs arrow" style="left:1098px;top:288px">›</div>
  <div class="abs testimonial" style="left:143px;top:184px;width:442px">
    <div class="mark">“</div>
    <p>Lorem ipsum dolor sit amet, consectetur adipiscing elit, sed do eiusmod tempor incididunt ut labore et dolore magna aliqua. Ut enim ad minim veniam, quis nostrud exercitation ullamco laboris nisi ut aliquip ex ea commodo consequat.</p>
    <div class="dash"></div><div class="who">MATEO</div>
  </div>
  <div class="abs testimonial" style="left:612px;top:184px;width:444px">
    <div class="mark">“</div>
    <p>Lorem ipsum dolor sit amet, consectetur adipiscing elit, sed do eiusmod tempor incididunt ut labore et dolore magna aliqua. Ut enim ad minim veniam, quis nostrud exercitation ullamco laboris nisi ut aliquip ex ea commodo consequat.</p>
    <div class="dash"></div><div class="who">MATEO</div>
  </div>
</section>

<!-- Contact -->
<section class="band" style="top:4011px;height:630px">
  <div class="abs section-head" style="top:30px">CONTACT US</div>
</section>
<div class="abs map" role="img" aria-label="Street map showing the agency location in Auckland"></div>
<div class="abs form">
  <h5>SEND MESSAGE</h5>
  <div class="ornament" role="img" aria-label="Small Maori-style ornament" style="width:44px;margin-top:8px"></div>
  <div class="field">NAME</div>
  <div class="field">E-MAIL</div>
  <div class="field">PHONE</div>
  <div class="field field-tall">MESSAGE</div>
  <div class="submit">SUBMIT</div>
</div>
<div class="abs contact-item" style="left:143px;top:4536px">
  <span class="ico"><svg width="16" height="20" viewBox="0 0 16 20"><path d="M8 1a6 6 0 0 1 6 6c0 5-6 12-6 12S2 12 2 7a6 6 0 0 1 6-6z" fill="#1d1d1d"/><circle cx="8" cy="7" r="2.2" fill="#fff"/></svg></span>
  <span>KOWHAI BAY<br>AUCKLAND</span>
</div>
<div class="abs contact-item" style="left:320px;top:4536px">
  <span class="ico"><svg width="18" height="18" viewBox="0 0 18 18"><path d="M4 1l3 4-2 2q2 4 6 6l2-2 4 3-2 3Q7 16 1 4z" fill="#1d1d1d"/></svg></span>
  <span>CALL US<br>+64 90 555 01234</span>
</div>
<div class="abs contact-item" style="left:530px;top:4536px">
  <span class="ico"><svg width="18" height="14" viewBox="0 0 18 14"><rect x="1" y="1" width="16" height="12" fill="none" stroke="#1d1d1d" stroke-width="1.6"/><path d="M1 1l8 7 8-7" fill="none" stroke="#1d1d1d" stroke-width="1.6"/></svg></span>
  <span>E-MAIL US<br>tessa@hireward.net</span>
</div>

<!-- Footer -->
<footer class="band band-dark" style="top:4641px;height:373px"></footer>
<div class="abs brand-badge" style="left:512px;top:4590px;width:176px;height:176px">Hireward.net</div>
<div class="abs follow">FOLLOW US
  <span class="social" role="img" aria-label="Social network link"></span>
  <span class="social" role="img" aria-label="Social network link"></span>
  <span class="social" role="img" aria-label="Social network link"></span>
</div>
<p class="abs copyright center">Copyright @ 2019 All Rights Reserved</p>

</body>
</html>
```